Verpackungen für Schwangerschaftsfotograf
sehr tolle und schnelle Umsetzungen meiner Wünsche - vielen Dank für die gute Zusammenarbeit
Zielgruppe
Fotograf mit Spezialisierung auf Schwangerschaft und Neugeborene
Aufgabenstellung
ich brauche ein Layout für diese Verpackung
https://www.faltwerk-muster.de/download/klappbox/Druckvorlage_FaltwerkMuster_Klappbox-30.pdf
ich stelle mir das vom Design her so vor wie eine Holzkiste:
https://www.bildervorrat-beispiel.com/de/image-photo/wooden-box-483910275?src=QkTzvLwe8pRnYd42h71xkc-1-27
Und wie der Text irgendwie mein Logo integrieren.
Die Schachtel soll eine neue Verpackung werden um Abzüge und USB Stick zu übergeben

```html
<!DOCTYPE html>
<html lang="de">
<head>
<meta charset="utf-8">
<title>Klappbox Holzkiste – Druckvorlage</title>
<link rel="stylesheet" href="https://fonts.googleapis.com/css2?family=Cinzel:wght@700&family=Crimson+Text:ital,wght@1,700&display=swap">
<style>
  :root {
    --paper: #ffffff;
    --wood-light: #e2b98e;
    --wood-mid: #c9925f;
    --wood-dark: #a86d42;
    --fold: #ec3d9a;
    --ink: #1a120c;
  }
  html, body {
    margin: 0;
    width: 1168px;
    height: 1200px;
    overflow: hidden;
    background: var(--paper);
  }
  .dieline {
    display: block;
    width: 1168px;
    height: 1200px;
  }
  .panel { fill: url(#woodGrain); }
  .panel--side { fill: url(#woodGrainSide); }
  .fold-line {
    fill: none;
    stroke: var(--fold);
    stroke-width: 1.2;
  }
  .brand-name {
    font-family: "Cinzel", serif;
    font-weight: 700;
    font-size: 15px;
    fill: var(--ink);
    letter-spacing: 0.5px;
  }
  .brand-url {
    font-family: "Crimson Text", serif;
    font-style: italic;
    font-weight: 700;
    font-size: 14px;
    fill: var(--ink);
    letter-spacing: 0.6px;
  }
  .brand-dot { fill: none; stroke: var(--ink); stroke-width: 2; }
</style>
</head>
<body>
<svg class="dieline" viewBox="0 0 1784 1838" preserveAspectRatio="none" xmlns="http://www.w3.org/2000/svg">
  <defs>
    <linearGradient id="woodGrain" x1="0" y1="0" x2="0" y2="1">
      <stop offset="0" stop-color="var(--wood-mid)"/>
      <stop offset="0.35" stop-color="var(--wood-light)"/>
      <stop offset="0.6" stop-color="var(--wood-dark)"/>
      <stop offset="1" stop-color="var(--wood-mid)"/>
    </linearGradient>
    <linearGradient id="woodGrainSide" x1="0" y1="0" x2="1" y2="0">
      <stop offset="0" stop-color="var(--wood-mid)"/>
      <stop offset="0.5" stop-color="var(--wood-light)"/>
      <stop offset="1" stop-color="var(--wood-dark)"/>
    </linearGradient>
  </defs>

  <g class="box-net" role="img" aria-label="Gestanzte Klappbox mit Altholz-Bretter-Textur">
    <!-- lid tuck flap with finger notch -->
    <path class="panel" d="M712 780 H1000 Q1018 780 1020 792 Q1030 812 1040 792 Q1042 780 1060 780 H1330 Q1352 780 1352 802 V850 Q1352 872 1330 872 H712 Q690 872 690 850 V802 Q690 780 712 780 Z"/>
    <!-- lid panel -->
    <rect class="panel" x="762" y="875" width="520" height="340"/>
    <!-- lid side flaps -->
    <path class="panel--side" d="M690 878 H762 V1210 H690 Q668 1210 668 1190 V898 Q668 878 690 878 Z"/>
    <path class="panel--side" d="M1282 878 H1354 Q1376 878 1376 898 V1190 Q1376 1210 1354 1210 H1282 Z"/>
    <!-- back wall strip -->
    <rect class="panel" x="578" y="1205" width="888" height="88" rx="18"/>
    <!-- base panel -->
    <rect class="panel" x="750" y="1298" width="543" height="338"/>
    <!-- base side walls with tabs -->
    <path class="panel--side" d="M575 1290 H750 V1640 H578 Q558 1640 558 1620 V1520 H550 V1470 H558 V1420 H550 V1370 H558 V1310 Q558 1290 575 1290 Z"/>
    <path class="panel--side" d="M1293 1290 H1468 Q1486 1290 1486 1310 V1370 H1492 V1420 H1486 V1470 H1492 V1520 H1486 V1620 Q1486 1640 1468 1640 H1293 Z"/>
    <!-- front wall strip -->
    <rect class="panel" x="578" y="1640" width="888" height="92" rx="18"/>
  </g>

  <g class="fold-lines">
    <path class="fold-line" d="M752 795 V872 M1290 795 V872 M704 805 V865 M1338 805 V865"/>
    <rect class="fold-line" x="762" y="875" width="520" height="340"/>
    <path class="fold-line" d="M680 890 V1200 M1366 890 V1200"/>
    <path class="fold-line" d="M590 1220 V1283 H1454 V1220 M752 1215 V1293 M1290 1215 V1293"/>
    <rect class="fold-line" x="750" y="1298" width="543" height="338"/>
    <path class="fold-line" d="M665 1300 V1630 M1380 1300 V1630 M570 1305 V1625 M1474 1305 V1625"/>
    <path class="fold-line" d="M590 1660 V1720 H1454 V1660 M755 1640 V1720 M1288 1640 V1720"/>
  </g>

  <!-- brand marks on lid (upside down, read when folded) -->
  <g class="brand-mark" transform="rotate(180 1125 845)">
    <circle class="brand-dot" cx="1002" cy="845" r="10"/>
    <text class="brand-name" x="1022" y="842">JONAS WEBERLING</text>
    <text class="brand-url" x="1022" y="860">babyfoto-musterstadt.de</text>
  </g>
  <g class="brand-mark" transform="rotate(180 1125 958)">
    <circle class="brand-dot" cx="1002" cy="958" r="10"/>
    <text class="brand-name" x="1022" y="955">JONAS WEBERLING</text>
    <text class="brand-url" x="1022" y="973">babyfoto-musterstadt.de</text>
  </g>
  <!-- brand mark on back wall -->
  <g class="brand-mark">
    <circle class="brand-dot" cx="1060" cy="1255" r="10"/>
    <text class="brand-name" x="1080" y="1255">JONAS WEBERLING</text>
    <text class="brand-url" x="1080" y="1271">babyfoto-musterstadt.de</text>
  </g>
</svg>
</body>
</html>
```